Company or website name
- Harborlight Advisory Partners
- Links to the website
- Harborlight-ap.example
- Describe your company and organization and target audience
- Harborlight specializes in providing executive recruiting/direct hire, contract/contract-to-hire, and project fulfillment services to clients at a national level, all while offering flexible pricing structures and solutions for companies based on their situation. Something very rare within the Staffing industry. The target audience is corporate leaders, managers. and Human Resources teams. This is not for candidates, only commercial, non-profit, end educational/government entities.
- The design should have the following
- I'm looking for both a tri-fold and 2 page brochure. PLEASE DO NOT ONLY USE THE BROCHURES I'VE PROVIDED. THESE ARE JUST FOR REFERENCE. THESE ARE BROCHURES I'VE CREATED AND AM NOT HAPPY WITH.
- Other Facts

```html
<!DOCTYPE html>
<html lang="en">
<head>
<meta charset="utf-8">
<title>Harborlight Advisory Partners – Brochure</title>
<link rel="stylesheet" href="https://fonts.googleapis.com/css2?family=Montserrat:wght@500;600&family=Roboto:ital,wght@0,400;0,500;1,300&display=swap">
<style>
  :root {
    --navy: #1c3b8e;
    --blue: #2857b0;
    --blue-deep: #173278;
    --paper: #f2f2f3;
    --ink: #3d3d42;
    --muted: #8a8c94;
    --stage: #e3e2e7;
    --photo-a: #4a62a0;
    --photo-b: #c9cfe0;
  }
  * { box-sizing: border-box; margin: 0; padding: 0; }
  html, body { width: 877px; height: 1200px; overflow: hidden; }
  body { background: var(--stage); font-family: "Roboto", sans-serif; color: var(--ink); position: relative; }

  .spread { position: absolute; left: 28px; width: 820px; height: 530px; display: flex; box-shadow: 0 8px 24px rgba(0,0,0,.12); }
  .spread--outer { top: 40px; }
  .spread--inner { top: 630px; }
  .page { position: relative; width: 410px; height: 530px; background: var(--paper); overflow: hidden; }
  .page + .page { border-left: 1px solid #dcdce0; }

  .brand { display: flex; align-items: center; gap: 8px; font-family: "Montserrat", sans-serif; font-weight: 500; color: var(--navy); letter-spacing: 2px; text-transform: uppercase; }
  .brand__dot { border-radius: 50%; background: var(--navy); flex: none; }

  /* Back cover */
  .back__brand { position: absolute; top: 42px; left: 0; right: 0; justify-content: center; font-size: 17px; }
  .back__brand .brand__dot { width: 18px; height: 18px; }
  .back__panel { position: absolute; top: 98px; left: 0; right: 0; height: 300px; background: var(--navy); color: #fff; text-align: center; padding: 38px 44px 0; }
  .back__panel::before { content: ""; position: absolute; left: 0; right: 0; top: 0; height: 14px; background: var(--blue-deep); }
  .quote { font-style: italic; font-weight: 300; font-size: 15px; line-height: 1.4; }
  .quote__by { margin-top: 8px; font-size: 8px; letter-spacing: 1px; text-transform: uppercase; }
  .contact { margin-top: 26px; font-size: 8.5px; line-height: 1.8; letter-spacing: .5px; text-transform: uppercase; }
  .contact__web { text-transform: none; }
  .back__tagline { position: absolute; top: 430px; left: 0; right: 0; text-align: center; color: var(--navy); font-size: 16px; font-weight: 500; line-height: 1.35; }

  /* Front cover */
  .front__brand { position: absolute; top: 38px; right: 40px; font-size: 28px; }
  .front__brand .brand__dot { width: 30px; height: 30px; }
  .band { position: absolute; left: 0; right: 0; background: var(--blue); color: #fff; font-size: 8.5px; letter-spacing: 3px; text-transform: uppercase; display: flex; align-items: center; justify-content: center; gap: 22px; }
  .band--services { top: 100px; height: 28px; }
  .band--motto { top: 352px; height: 28px; }
  .front__photo { position: absolute; top: 128px; left: 0; right: 0; height: 224px; background: linear-gradient(135deg, var(--photo-a), var(--photo-b) 60%, #5d6fa8); }
  .front__text { position: absolute; top: 398px; left: 26px; right: 14px; display: flex; flex-direction: column; gap: 6px; }
  .front__headline { font-size: 17px; line-height: 1.25; color: var(--ink); }
  .front__sub { font-size: 15px; line-height: 1.25; color: var(--blue); }

  /* Inner left */
  .inner-left__photo { position: absolute; top: 0; left: 0; right: 0; height: 160px; background: linear-gradient(120deg, #7a8296, #2b2f3c 55%, #a9b0bf); }
  .copy { position: absolute; top: 178px; left: 28px; width: 228px; }
  .copy h2, .copy h3 { color: var(--navy); font-weight: 500; }
  .copy h2 { font-size: 11px; margin-bottom: 6px; }
  .copy h3 { font-size: 10.5px; margin: 12px 0 5px; }
  .copy p { font-size: 7.5px; line-height: 1.5; color: #6b6d74; margin-bottom: 5px; }
  .inner-left__circle { position: absolute; top: 318px; left: 268px; width: 130px; height: 130px; border-radius: 50%; border: 4px solid var(--navy); background: radial-gradient(circle, #c89f86, #4a5c8e 75%); }
  .footer-strip { position: absolute; bottom: 0; left: 0; right: 0; height: 20px; background: var(--navy); color: #fff; font-size: 7.5px; display: flex; align-items: center; padding: 0 24px; }
  .footer-strip--right { justify-content: flex-end; }

  /* Inner right */
  .inner-right__head { position: absolute; top: 0; left: 0; right: 0; height: 150px; background: var(--blue); color: #fff; padding: 30px 28px 0; }
  .inner-right__head .brand { color: #fff; font-size: 15px; }
  .inner-right__head .brand__dot { width: 14px; height: 14px; background: #fff; }
  .inner-right__head h2 { font-size: 14px; font-weight: 500; margin: 12px 0 6px; }
  .inner-right__head p { font-size: 8px; line-height: 1.5; opacity: .9; }
  .hub { position: absolute; top: 318px; left: 173px; width: 64px; height: 64px; border-radius: 50%; background: var(--navy); }
  .service { position: absolute; width: 108px; }
  .service h4 { display: flex; align-items: center; gap: 4px; font-size: 8px; font-weight: 500; color: var(--navy); margin-bottom: 3px; }
  .service h4::before { content: ""; width: 8px; height: 8px; border-radius: 50%; background: var(--navy); flex: none; }
  .service p { font-size: 6.5px; line-height: 1.45; color: var(--muted); padding-left: 12px; }
</style>
</head>
<body>

<section class="spread spread--outer">
  <article class="page back">
    <div class="brand back__brand"><span class="brand__dot"></span>Harborlight</div>
    <div class="back__panel">
      <p class="quote">“We must open the doors of Opportunity. But we must also equip our people to walk through those doors.”</p>
      <p class="quote__by">Marcus Ellery</p>
      <p class="contact">480 Meridian Plaza Ste 210<br>Easton, NY 10000<br>555.010.2746<br><span class="contact__web">www.harborlight-ap.example</span></p>
    </div>
    <p class="back__tagline">Harborlight consulting provides<br>total end to end staffing solutions</p>
  </article>

  <article class="page front">
    <div class="brand front__brand"><span class="brand__dot"></span>Harborlight</div>
    <div class="band band--services"><span>Staffing</span><span>|</span><span>Exec Recruiting</span><span>|</span><span>Consulting</span></div>
    <div class="front__photo" role="img" aria-label="Photo of a hand moving a chess piece on a board"></div>
    <div class="band band--motto"><span>Simplifying Staffing</span></div>
    <div class="front__text">
      <p class="front__headline">Flexible Solutions for your business needs</p>
      <p class="front__sub">We provide total end to end staffing solutions</p>
    </div>
  </article>
</section>

<section class="spread spread--inner">
  <article class="page inner-left">
    <div class="inner-left__photo" role="img" aria-label="Photo of a business team standing together in an office"></div>
    <div class="copy">
      <h2>Connecting your Business to the resources you need</h2>
      <p>Harborlight Staffing specializes in direct hire, contract and project fulfillment. We learn your goals, your culture and your challenges, then build a search plan that delivers vetted talent quickly and keeps every engagement transparent.</p>
      <p>Our goal is to partner with your leadership team, respond with urgency and support every requirement promptly and thoroughly.</p>
      <h3>Project Consultation</h3>
      <p>Our consultants bring the expertise needed to scope critical initiatives. We assess your current state, recommend the right staffing mix and plan delivery that supports your budget, timeline and long term growth.</p>
      <h3>Personal Approach</h3>
      <p>The better we get to know your needs, the easier it is for us to connect you to the right people. We match qualified professionals with positions that truly fit their skill set.</p>
    </div>
    <div class="inner-left__circle" role="img" aria-label="Circular photo of colleagues huddled together looking down at the camera"></div>
    <div class="footer-strip">www.harborlight-ap.example</div>
  </article>

  <article class="page inner-right">
    <div class="inner-right__head">
      <div class="brand"><span class="brand__dot"></span>Harborlight</div>
      <h2>Connecting your Business to the resources you need</h2>
      <p>Flexible pricing and national reach let us shape each engagement around your situation, from a single critical hire to a full project team.</p>
    </div>
    <div class="hub"></div>
    <div class="service" style="top:178px;left:160px"><h4>Contract Staffing</h4><p>Skilled contractors ready for short or long terms.</p></div>
    <div class="service" style="top:212px;left:40px"><h4>Retained Search</h4><p>Dedicated search for senior and niche leadership roles.</p></div>
    <div class="service" style="top:262px;left:272px"><h4>Staff Augmentation</h4><p>Extra capacity that blends with your current team.</p></div>
    <div class="service" style="top:282px;left:30px"><h4>Temp Staffing</h4><p>Reliable temporary talent when demand suddenly rises.</p></div>
    <div class="service" style="top:338px;left:272px"><h4>Executive Search</h4><p>Confidential outreach to proven executive leaders nationwide.</p></div>
    <div class="service" style="top:360px;left:28px"><h4>Project Based Staffing</h4><p>Complete teams assembled for defined project goals.</p></div>
    <div class="service" style="top:410px;left:262px"><h4>Project Planning</h4><p>Scoping, budgeting and timelines built with you.</p></div>
    <div class="service" style="top:438px;left:120px"><h4>Contract-to-Hire</h4><p>Evaluate talent on the job before committing.</p></div>
    <div class="footer-strip footer-strip--right">www.harborlight-ap.example</div>
  </article>
</section>

</body>
</html>
```